business card

Business card for new business.
Red and black corporate colors.
Card can have an Indsutrial feel to it. Feel free to add Rust, Bolted steel, or graphics as you see fit. We provide highly specialized services to the below mentioned industries.
Keep information out of corners so that if I want I can choose rounded corners.
Information
- front. name - title - phone - email
- Rear
Pipelines - Marine - Utilities - Forestry - Power
Regina - Saskatoon - Lethbridge - Kamloops - Prince George

```html
<!DOCTYPE html>
<html lang="en">
<head>
<meta charset="utf-8">
<title>Kestrelworks business card</title>
<link rel="stylesheet" href="https://fonts.googleapis.com/css2?family=Roboto:wght@400;500;900&display=swap">
<style>
  :root {
    --stage: #2b2b2d;
    --steel: #6d6d72;
    --paper: #ffffff;
    --signal-red: #e31b23;
    --ink-light: #f2f2f2;
    --ink-soft: #dcdcdf;
  }
  * { box-sizing: border-box; margin: 0; padding: 0; }
  html, body {
    width: 1200px; height: 900px; overflow: hidden;
    background: var(--stage);
    font-family: "Roboto", Arial, sans-serif;
  }
  .sheet {
    width: 1200px; height: 900px;
    display: flex; flex-direction: column; align-items: center; justify-content: center;
    gap: 56px;
  }
  .card {
    position: relative;
    width: 640px; height: 366px;
    border-radius: 26px;
    overflow: hidden;
  }

  /* Front */
  .card-front { background: var(--paper); }
  .front-band {
    position: absolute; inset: 0;
    background: var(--steel);
    clip-path: polygon(0 47%, 100% 60%, 100% 100%, 0 100%);
  }
  .brand-name {
    font-weight: 900; text-transform: uppercase; letter-spacing: 1px;
    line-height: 1; white-space: nowrap;
  }
  .card-front .brand-name {
    position: absolute; top: 52px; left: 0; right: 0;
    text-align: center; font-size: 62px; color: var(--steel);
  }
  .name-plate {
    position: absolute; left: 168px; top: 150px;
    width: 262px; padding: 12px 0 10px;
    background: var(--signal-red); color: var(--paper);
    text-align: center;
  }
  .name-plate .person { font-size: 25px; font-weight: 500; text-transform: uppercase; letter-spacing: .5px; }
  .name-plate .role { font-size: 15px; margin-top: 3px; }
  .contact-list {
    position: absolute; left: 38px; bottom: 44px;
    list-style: none; color: var(--ink-light); font-size: 15px;
  }
  .contact-list li { display: flex; align-items: center; gap: 8px; margin-top: 5px; }
  .contact-list svg { width: 11px; height: 11px; fill: none; stroke: var(--ink-light); stroke-width: 1.6; }
  .address {
    position: absolute; right: 44px; bottom: 40px;
    color: var(--ink-light); font-size: 18px; line-height: 1.35; text-align: left;
    font-style: normal;
  }

  /* Back */
  .card-back { background: var(--steel); }
  .card-back .brand-name {
    position: absolute; top: 104px; left: 0; right: 0;
    text-align: center; font-size: 70px; color: var(--paper);
  }
  .service-lines {
    position: absolute; top: 224px; left: 0; right: 0;
    text-align: center; color: var(--ink-soft); font-size: 16px; line-height: 1.6;
    letter-spacing: .3px;
  }
</style>
</head>
<body>
<main class="sheet">
  <section class="card card-front" aria-label="Card front">
    <div class="front-band"></div>
    <div class="brand-name">Kestrelworks</div>
    <div class="name-plate">
      <div class="person">Daniel Reyes</div>
      <div class="role">Director</div>
    </div>
    <ul class="contact-list">
      <li><svg viewBox="0 0 12 12"><path d="M3 1 L5 3.5 L4 5 Q5 7 7 8 L8.5 7 L11 9 L9.5 11 Q2 10 1 2.5 Z"/></svg>+330 5512-4870</li>
      <li><svg viewBox="0 0 12 12"><rect x="1" y="2.5" width="10" height="7"/><path d="M1 2.5 L6 6.5 L11 2.5"/></svg>info@kestrelworks.com</li>
      <li><svg viewBox="0 0 12 12"><circle cx="6" cy="6" r="5"/><path d="M1 6 H11 M6 1 Q3 6 6 11 M6 1 Q9 6 6 11"/></svg>www.kestrelworks.com</li>
    </ul>
    <address class="address">2290 Ironwood Ave.<br>Denver, CO 80216</address>
  </section>

  <section class="card card-back" aria-label="Card back">
    <div class="brand-name">Kestrelworks</div>
    <p class="service-lines">
      Pipelines - Marine - Utilities - Forestry - Power<br>
      Regina - Saskatoon - Lethbridge - Kamloops - Prince George
    </p>
  </section>
</main>
</body>
</html>
```